Psychotherapist's business card

I need a business card design for a psychotherapist. I expect business card to have "light" design. By this I mean that it can somehow translate easiness, serenity. Maybe pastel colours can help you here. I have attached some pictures from Greece. Perhaps they can inspire you to combine colours and to achieve that "light" design.
Updates

Pls, don't use any free samples you may find on business card generators. It looks too simple, uncreative and waste of time! READ size and colour requirements! I don't want to see any shapes like rings, triangles etc.

Contact Information for Business Card

Size: 65mmX60mm

Name - Мирослав Гречихин

Психолог
+7(916)482-39-07
grechikhin.com

I suppose that thin font can look good but it's up to you

Requirements
Must have
• size requirements
Nice to have
• pastel colours
• thin font
Should not have
• black and dark colours
• lines, free design samples used from other web-sites

```html
<!DOCTYPE html>
<html lang="ru">
<head>
<meta charset="utf-8">
<title>Мирослав Гречихин — визитка</title>
<link rel="stylesheet" href="https://fonts.googleapis.com/css2?family=PT+Serif:wght@400&display=swap">
<style>
  :root {
    --backdrop: #6aa3d3;
    --card-paper: #f4f3ef;
    --sun-yellow: #d6d25a;
    --sea-dots: #b9e2da;
    --coral-pink: #f0b9a2;
    --ink-blue: #1d5a9e;
  }
  * { margin: 0; padding: 0; box-sizing: border-box; }
  html, body {
    width: 1200px;
    height: 960px;
    overflow: hidden;
  }
  body {
    background: var(--backdrop);
    display: flex;
    align-items: center;
    justify-content: center;
    font-family: "PT Serif", Georgia, serif;
  }
  /* 65 × 60 mm at 10 px per mm */
  .business-card {
    position: relative;
    width: 650px;
    height: 600px;
    background: var(--card-paper);
    overflow: hidden;
    box-shadow: 0 18px 40px rgba(20, 60, 110, 0.25);
  }
  .block { position: absolute; }
  .block--dots-top {
    left: 300px; top: 36px; width: 300px; height: 130px;
    background: var(--sea-dots);
  }
  .block--yellow {
    left: 0; top: 80px; width: 380px; height: 190px;
    background: var(--sun-yellow);
  }
  .block--pink {
    left: 440px; top: 380px; width: 210px; height: 90px;
    background: var(--coral-pink);
  }
  .block--dots-bottom {
    left: 0; top: 470px; width: 520px; height: 92px;
    background: var(--sea-dots);
  }
  .contact {
    position: absolute;
    left: 42px;
    top: 292px;
    color: var(--ink-blue);
  }
  .contact__name {
    font-size: 30px;
    font-weight: 400;
    letter-spacing: 0.04em;
    line-height: 1.1;
  }
  .contact__role-en {
    font-size: 18px;
    line-height: 1.2;
  }
  .contact__details {
    margin-top: 26px;
    font-size: 18px;
    line-height: 1.25;
    list-style: none;
  }
</style>
</head>
<body>
  <article class="business-card">
    <div class="block block--dots-top" role="img" aria-label="Мятный точечный растр"></div>
    <div class="block block--yellow"></div>
    <div class="block block--pink"></div>
    <div class="block block--dots-bottom" role="img" aria-label="Мятный точечный растр"></div>

    <div class="contact">
      <h1 class="contact__name">Мирослав Гречихин</h1>
      <p class="contact__role-en">psychotherapist.</p>
      <ul class="contact__details">
        <li>Психолог</li>
        <li>+7(916)482-39-07</li>
        <li>grechikhin.com</li>
      </ul>
    </div>
  </article>
</body>
</html>
```